Business Cards

Business card design for my company.
I would like the card's background colour to be black. You can also see our web site to get an idea of our brand. https://www.dlqmarrowfield.com.au/
- Name
- Email

```html
<!DOCTYPE html>
<html lang="en">
<head>
<meta charset="utf-8">
<title>DLQ Marrowfield — Business Cards</title>
<link href="https://fonts.googleapis.com/css2?family=Montserrat:wght@400;500;700&display=swap" rel="stylesheet">
<style>
  :root {
    --stage: #2a2a2a;
    --card: #1d1d1d;
    --green: #0f9a45;
    --white: #f2f2f2;
    --muted: #cfcfcf;
    --pattern-dark: #141414;
    --pattern-light: #3a3a3a;
  }
  * { margin: 0; padding: 0; box-sizing: border-box; }
  html, body { width: 1200px; height: 875px; overflow: hidden; }
  body {
    background: var(--stage);
    font-family: "Montserrat", sans-serif;
    position: relative;
  }
  .card {
    position: absolute;
    width: 510px;
    height: 300px;
    border-radius: 16px;
    background: var(--card);
    overflow: hidden;
    box-shadow: 0 20px 40px rgba(0,0,0,0.45);
  }
  .card--back { left: 60px; top: 130px; }
  .card--front { left: 630px; top: 445px; }

  .back-pattern {
    position: absolute; inset: 0;
    background: linear-gradient(120deg, var(--pattern-light) 0%, var(--pattern-dark) 70%);
  }
  .back-mark {
    position: absolute; right: 34px; top: 120px;
    display: flex; align-items: center; gap: 6px;
    color: var(--white); font-weight: 700; font-size: 13px; letter-spacing: 0.5px;
  }
  .back-mark .dot { width: 8px; height: 8px; background: var(--green); }

  .brand {
    position: absolute; right: 36px; top: 34px;
    display: flex; align-items: center; gap: 10px;
    color: var(--white); font-weight: 700; font-size: 24px; letter-spacing: 1px;
  }
  .brand .dot { width: 14px; height: 14px; background: var(--green); }

  .divider {
    position: absolute; left: 30px; top: 160px;
    width: 450px; height: 1px; background: var(--green);
  }
  .person { position: absolute; left: 30px; top: 104px; }
  .person__name {
    color: var(--green); font-weight: 700; font-size: 26px; letter-spacing: 0.5px; text-transform: uppercase;
  }
  .person__role { color: var(--muted); font-size: 13px; margin-top: 2px; }

  .contacts { position: absolute; left: 30px; top: 176px; list-style: none; }
  .contacts li {
    display: flex; align-items: center; gap: 10px;
    color: var(--white); font-size: 13px; line-height: 22px;
  }
  .contacts svg { width: 11px; height: 11px; fill: var(--green); flex: none; }

  .base-band {
    position: absolute; left: 0; bottom: 0; width: 100%; height: 16px;
    display: flex;
  }
  .base-band .green { flex: 1; background: var(--green); }
  .base-band .white { width: 110px; background: var(--white); }
</style>
</head>
<body>
  <section class="card card--back" aria-label="Card back">
    <div class="back-pattern" role="img" aria-label="Repeating company mark pattern in graded silver to black"></div>
    <div class="back-mark"><span class="dot"></span>DLQ MARROWFIELD</div>
  </section>

  <section class="card card--front" aria-label="Card front">
    <div class="brand"><span class="dot"></span>DLQ MARROWFIELD</div>

    <div class="person">
      <h1 class="person__name">Dale Hartwell</h1>
      <p class="person__role">General Manager</p>
    </div>
    <div class="divider"></div>

    <ul class="contacts">
      <li>
        <svg viewBox="0 0 24 24"><path d="M6.6 10.8a15 15 0 0 0 6.6 6.6l2.2-2.2a1 1 0 0 1 1-.25 11 11 0 0 0 3.6.6 1 1 0 0 1 1 1V20a1 1 0 0 1-1 1A17 17 0 0 1 3 4a1 1 0 0 1 1-1h3.5a1 1 0 0 1 1 1 11 11 0 0 0 .6 3.6 1 1 0 0 1-.25 1z"/></svg>
        0400 555 182
      </li>
      <li>
        <svg viewBox="0 0 24 24"><path d="M2 5h20v14H2z M2 5l10 8 10-8" /></svg>
        info@dlqmarrowfield.com.au
      </li>
      <li>
        <svg viewBox="0 0 24 24"><circle cx="12" cy="12" r="10"/></svg>
        dlqmarrowfield.com.au
      </li>
    </ul>

    <div class="base-band"><span class="green"></span><span class="white"></span></div>
  </section>
</body>
</html>
```